Voltmark Advisory Grupe Stationary
business cards, letter head, envelopes, fax sheet and shipping label
Voltmark Advisory Grupe Stationary - Energy
Creative Brief
Professional
Tom Wellsby
Operations Manager
Voltmark Advisory Group C/o Miles R. Dunstan Esq., Coral Court and West Ridge Road P.O. Box K-57819
office - 242-555-0193
twellsby@voltmarkadvisorygroup.example
www.voltmarkadvisorygroup.example
USA Cel # 832-555-0146

```html
<!DOCTYPE html>
<html lang="en">
<head>
<meta charset="utf-8">
<title>Voltmark Advisory Group Stationery</title>
<link rel="stylesheet" href="https://fonts.googleapis.com/css2?family=Open+Sans:wght@400;600;700&display=swap">
<style>
  :root {
    --orange: #f5a31a;
    --blue: #1f6fb5;
    --ink: #3a3f45;
    --muted: #7a8088;
    --paper: #ffffff;
    --backdrop: #e8e5df;
  }
  * { box-sizing: border-box; margin: 0; padding: 0; }
  html, body { width: 1200px; height: 602px; overflow: hidden; }
  body {
    background: var(--backdrop);
    font-family: "Open Sans", Arial, sans-serif;
    color: var(--ink);
    position: relative;
  }
  .sheet {
    position: absolute;
    background: var(--paper);
    box-shadow: 0 2px 6px rgba(0,0,0,.18);
    overflow: hidden;
  }
  .brand { display: flex; align-items: center; gap: 5px; }
  .brand-square { width: 14px; height: 14px; background: var(--orange); flex: none; }
  .brand-name {
    font-weight: 700; color: var(--blue);
    font-size: 9px; line-height: 1.05; letter-spacing: .02em; text-transform: uppercase;
    white-space: nowrap;
  }
  .band { position: absolute; left: 0; right: 0; bottom: 0; height: 6px; display: flex; }
  .band .o { width: 30%; background: var(--orange); }
  .band .b { flex: 1; background: var(--blue); }

  /* business cards */
  .card { width: 200px; height: 114px; padding: 10px 12px; }
  .card .person { position: absolute; left: 12px; top: 40px; }
  .card .person-name { font-weight: 700; font-size: 9px; color: var(--ink); }
  .card .person-title { font-size: 6.5px; color: var(--muted); }
  .card .contact {
    position: absolute; right: 8px; top: 40px; width: 110px;
    font-size: 5px; line-height: 1.5; color: var(--ink); white-space: nowrap;
  }
  .card .contact b { color: var(--blue); font-weight: 600; }
  .card-back { width: 200px; height: 114px; display: flex; align-items: center; justify-content: center; }
  .card-back .brand-square { width: 20px; height: 20px; }
  .card-back .brand-name { font-size: 12px; }
  .card-back .web { position: absolute; bottom: 12px; width: 100%; text-align: center; font-size: 6px; color: var(--muted); }

  /* letterhead */
  .letterhead { left: 470px; top: 28px; width: 270px; height: 350px; padding: 18px 20px; }
  .letterhead .brand-square { width: 16px; height: 16px; }
  .letterhead .brand-name { font-size: 9.5px; }
  .letterhead .sender {
    position: absolute; right: 20px; top: 18px; width: 90px;
    font-size: 5px; line-height: 1.5; color: var(--muted); white-space: nowrap;
  }
  .letterhead .footer {
    position: absolute; left: 20px; right: 20px; bottom: 12px;
    display: grid; grid-template-columns: auto auto; row-gap: 2px;
    justify-content: space-between;
    font-size: 5px; line-height: 1.3; color: var(--muted); white-space: nowrap;
  }
  .letterhead .footer .web { grid-column: 1 / -1; }
  .letterhead .band { height: 4px; bottom: 34px; left: 20px; right: 20px; }

  /* envelopes */
  .envelope-back { left: 780px; top: 110px; width: 360px; height: 160px; }
  .envelope-back svg { position: absolute; inset: 0; }
  .envelope-back .brand { position: absolute; left: 150px; top: 60px; }
  .envelope-back .brand-square { width: 18px; height: 18px; }
  .envelope-back .brand-name { font-size: 10px; }
  .envelope-front { left: 780px; top: 300px; width: 360px; height: 160px; padding: 14px 16px; }
  .envelope-front .brand-square { width: 16px; height: 16px; }
  .envelope-front .brand-name { font-size: 10px; }
  .envelope-front .return {
    position: absolute; left: 16px; top: 38px; font-size: 5.5px; line-height: 1.5; color: var(--muted);
  }
  .envelope-front .web { position: absolute; right: 16px; bottom: 16px; font-size: 6px; color: var(--blue); }
</style>
</head>
<body>

  <section class="sheet card" style="left:40px;top:140px;">
    <div class="brand"><span class="brand-square"></span><span class="brand-name">Voltmark<br>Advisory Group</span></div>
    <div class="person"><div class="person-name">Tom Wellsby</div><div class="person-title">Operations Manager</div></div>
    <div class="contact">
      <b>office</b> 242-555-0193<br>
      <b>USA Cel #</b> 832-555-0146<br>
      twellsby@voltmarkadvisorygroup.example<br>
      www.voltmarkadvisorygroup.example
    </div>
    <div class="band"><span class="o"></span><span class="b"></span></div>
  </section>

  <section class="sheet card" style="left:255px;top:140px;">
    <div class="brand"><span class="brand-square"></span><span class="brand-name">Voltmark<br>Advisory Group</span></div>
    <div class="person"><div class="person-name">Tom Wellsby</div><div class="person-title">Operations Manager</div></div>
    <div class="contact">
      C/o Miles R. Dunstan Esq.<br>
      Coral Court and West Ridge Road<br>
      P.O. Box K-57819<br>
      <b>office</b> 242-555-0193
    </div>
    <div class="band"><span class="o"></span><span class="b"></span></div>
  </section>

  <section class="sheet card" style="left:40px;top:275px;">
    <div class="brand"><span class="brand-square"></span><span class="brand-name">Voltmark<br>Advisory Group</span></div>
    <div class="person"><div class="person-name">Tom Wellsby</div><div class="person-title">Operations Manager</div></div>
    <div class="contact">
      <b>office</b> 242-555-0193<br>
      <b>USA Cel #</b> 832-555-0146<br>
      twellsby@voltmarkadvisorygroup.example
    </div>
    <div class="band"><span class="o"></span><span class="b"></span></div>
  </section>

  <section class="sheet card" style="left:255px;top:275px;">
    <div class="brand"><span class="brand-square"></span><span class="brand-name">Voltmark<br>Advisory Group</span></div>
    <div class="person"><div class="person-name">Tom Wellsby</div><div class="person-title">Operations Manager</div></div>
    <div class="contact">
      Coral Court and West Ridge Road<br>
      P.O. Box K-57819<br>
      www.voltmarkadvisorygroup.example
    </div>
    <div class="band"><span class="o"></span><span class="b"></span></div>
  </section>

  <section class="sheet card-back" style="left:147px;top:415px;">
    <div class="brand"><span class="brand-square"></span><span class="brand-name">Voltmark<br>Advisory Group</span></div>
    <div class="web">www.voltmarkadvisorygroup.example</div>
  </section>

  <section class="sheet letterhead">
    <div class="brand"><span class="brand-square"></span><span class="brand-name">Voltmark<br>Advisory Group</span></div>
    <div class="sender">
      Voltmark Advisory Group<br>
      C/o Miles R. Dunstan Esq.<br>
      Coral Court and West Ridge Road<br>
      P.O. Box K-57819
    </div>
    <div class="band"><span class="o"></span><span class="b"></span></div>
    <div class="footer">
      <span>office 242-555-0193</span>
      <span>twellsby@voltmarkadvisorygroup.example</span>
      <span class="web">www.voltmarkadvisorygroup.example</span>
    </div>
  </section>

  <section class="sheet envelope-back">
    <svg width="360" height="160" viewBox="0 0 360 160">
      <polyline points="0,0 180,95 360,0" fill="none" stroke="#d9dde2" stroke-width="1.5"/>
      <polyline points="0,160 150,70" fill="none" stroke="#e3e6ea" stroke-width="1"/>
      <polyline points="360,160 210,70" fill="none" stroke="#e3e6ea" stroke-width="1"/>
    </svg>
    <div class="brand"><span class="brand-square"></span><span class="brand-name">Voltmark<br>Advisory Group</span></div>
  </section>

  <section class="sheet envelope-front">
    <div class="brand"><span class="brand-square"></span><span class="brand-name">Voltmark<br>Advisory Group</span></div>
    <div class="return">
      C/o Miles R. Dunstan Esq., Coral Court and West Ridge Road<br>
      P.O. Box K-57819
    </div>
    <div class="web">www.voltmarkadvisorygroup.example</div>
    <div class="band"><span class="o"></span><span class="b"></span></div>
  </section>

</body>
</html>
```